Need webdesign for service company that provides Car hiring service and transit service

We need a web design for a company that provides airport transit services and transport services including Limo, Corporate cars, Disability transit, Family transit service. We need is a simple and professional design.

Below is site which we like and also offer the same service http://www.ridelyntrek.com.au/

Reason: Waiting for the Feedback from multiple stakeholders. Need the time to select and approve the design

Target Market(s)

Tourism, Travel

Industry/Entity Type

Airport

Number of Pages Required

3 page

Font styles to use
Decorative
Script

Requirements
Must have
• Simple and Professional, Site we like http://www.ridelyntrek.com.au/ and also need to mobile friendly
Should not have
• Shouldn't have too many images

```html
<!DOCTYPE html>
<html lang="en">
<head>
<meta charset="utf-8">
<title>RIDEWAY – Private &amp; Business Transport</title>
<link href="https://fonts.googleapis.com/css2?family=Poppins:wght@300;400;500&family=Source+Sans+3:wght@400;600&display=swap" rel="stylesheet">
<style>
  :root {
    --ink: #111111;
    --text: #333333;
    --muted: #555555;
    --panel: #0d0d0d;
    --icon-box: #2f2f2f;
    --button: #757071;
    --line: #dddddd;
    --band: #f6f6f6;
    --frame: #d6d6d6;
    --white: #ffffff;
  }
  * { box-sizing: border-box; margin: 0; padding: 0; }
  html, body { width: 1095px; height: 1200px; overflow: hidden; background: var(--white); }
  body { font-family: "Poppins", sans-serif; color: var(--text); }
  .page { position: relative; width: 1095px; height: 1200px; overflow: hidden; }
  .abs { position: absolute; }

  /* Header */
  .site-header { position: absolute; left: 0; top: 0; width: 1095px; height: 110px; border-bottom: 1px solid var(--line); box-shadow: 0 6px 14px -10px rgba(0,0,0,.18); }
  .brand { position: absolute; left: 71px; top: 36px; display: flex; align-items: center; gap: 12px; }
  .brand-mark { width: 26px; height: 26px; background: var(--icon-box); }
  .brand-name { font-family: "Poppins", sans-serif; font-weight: 400; font-size: 32px; letter-spacing: 0.5px; color: var(--text); line-height: 1; }
  .social { position: absolute; left: 695px; top: 41px; display: flex; gap: 11px; }
  .social span { width: 17px; height: 16px; background: #e6e6e6; border-radius: 2px; display: block; }
  .menu-btn { position: absolute; left: 807px; top: 32px; width: 35px; height: 32px; background: var(--icon-box); border-radius: 3px; display: flex; align-items: center; justify-content: center; }
  .search-btn { position: absolute; left: 848px; top: 32px; width: 35px; height: 32px; border: 1px solid var(--line); border-radius: 3px; display: flex; align-items: center; justify-content: center; }
  .phone-box { position: absolute; left: 890px; top: 32px; width: 132px; height: 32px; border: 1px solid var(--line); border-radius: 3px; display: flex; align-items: center; justify-content: space-between; padding: 0 7px 0 9px; font-family: "Source Sans 3", sans-serif; font-weight: 600; font-size: 15px; color: var(--ink); }
  .phone-icon { width: 20px; height: 20px; border-radius: 50%; background: #9a9a9a; display: flex; align-items: center; justify-content: center; }

  /* Hero */
  .hero-title { position: absolute; left: 0; top: 138px; width: 1095px; text-align: center; font-size: 26px; font-weight: 400; letter-spacing: 1px; color: var(--ink); }
  .hero-sub { position: absolute; left: 0; top: 173px; width: 1095px; text-align: center; font-size: 12px; font-weight: 400; letter-spacing: 0.6px; color: var(--ink); }

  .quote-panel { position: absolute; left: 75px; top: 214px; width: 298px; height: 321px; background: var(--panel); }
  .quote-title { position: absolute; left: 0; top: 26px; width: 100%; text-align: center; color: var(--white); font-size: 21px; font-weight: 400; letter-spacing: 0.4px; }
  .quote-title b { font-weight: 500; }
  .field { position: absolute; left: 12px; width: 275px; background: var(--white); border-radius: 2px; font-size: 12px; color: var(--text); padding-left: 13px; display: flex; align-items: center; }
  .field-origin { top: 86px; height: 36px; }
  .field-dest { top: 131px; height: 36px; }
  .field-vehicles { top: 178px; height: 68px; display: block; padding-top: 16px; }
  .field-vehicles .add { margin-top: 7px; padding-left: 6px; display: flex; gap: 14px; }
  .cta { position: absolute; left: 9px; top: 256px; width: 276px; height: 41px; background: var(--button); border-radius: 2px; color: var(--white); font-size: 16px; font-weight: 500; letter-spacing: 0.6px; display: flex; align-items: center; justify-content: center; }

  .hero-photo { position: absolute; left: 394px; top: 212px; width: 628px; height: 323px; background: linear-gradient(135deg, #8a9aa0 0%, #4a5357 40%, #1b1419 70%, #3c4448 100%); }

  /* Services */
  .service { position: absolute; top: 688px; width: 221px; height: 156px; border: 2px solid #e3e3e3; text-align: center; }
  .service-icon { position: absolute; top: -21px; left: 76px; width: 70px; height: 45px; background: var(--icon-box); display: flex; align-items: center; justify-content: center; }
  .service h3 { margin-top: 40px; font-size: 16px; font-weight: 300; letter-spacing: 0.4px; color: var(--ink); white-space: nowrap; }
  .service h3 b { font-weight: 500; }
  .service p { margin: 8px auto 0; width: 196px; font-size: 11.3px; line-height: 18px; font-weight: 300; color: var(--muted); }

  /* About */
  .about { position: absolute; left: 0; top: 889px; width: 1095px; height: 219px; background: var(--band); }
  .about h2 { position: absolute; left: 74px; top: 27px; font-family: "Source Sans 3", sans-serif; font-weight: 400; font-size: 25px; color: var(--ink); letter-spacing: 0.3px; }
  .about p { position: absolute; left: 74px; top: 69px; width: 575px; font-family: "Source Sans 3", sans-serif; font-size: 12.3px; line-height: 23px; color: var(--text); }
  .about-frame { position: absolute; left: 700px; top: 36px; width: 314px; height: 167px; background: var(--frame); padding: 7px; }
  .about-photo { width: 100%; height: 100%; background: linear-gradient(160deg, #9ea3a7 0%, #5d6266 45%, #161616 75%, #44484b 100%); }

  /* Footer */
  .site-footer { position: absolute; left: 0; top: 1155px; width: 1095px; height: 45px; background: var(--frame); display: flex; align-items: center; justify-content: center; font-size: 13px; color: var(--ink); }
</style>
</head>
<body>
<div class="page">

  <header class="site-header">
    <div class="brand">
      <span class="brand-mark"></span>
      <span class="brand-name">RIDEWAY</span>
    </div>
    <nav class="social" aria-label="Social links">
      <span></span><span></span><span></span><span></span>
    </nav>
    <div class="menu-btn" aria-label="Menu">
      <svg width="12" height="11" viewBox="0 0 12 11"><rect y="0" width="12" height="2" fill="#fff"/><rect y="4.5" width="12" height="2" fill="#fff"/><rect y="9" width="12" height="2" fill="#fff"/></svg>
    </div>
    <div class="search-btn" aria-label="Search">
      <svg width="14" height="14" viewBox="0 0 14 14"><circle cx="5.5" cy="5.5" r="4.3" fill="none" stroke="#333" stroke-width="1.6"/><line x1="8.6" y1="8.6" x2="13" y2="13" stroke="#333" stroke-width="1.8"/></svg>
    </div>
    <div class="phone-box">
      <span>123-456-7890</span>
      <span class="phone-icon">
        <svg width="11" height="11" viewBox="0 0 24 24"><path d="M6.6 10.8a15 15 0 0 0 6.6 6.6l2.2-2.2c.3-.3.7-.4 1-.2 1.1.4 2.3.6 3.6.6.6 0 1 .4 1 1V20c0 .6-.4 1-1 1C10.6 21 3 13.4 3 4c0-.6.4-1 1-1h3.5c.6 0 1 .4 1 1 0 1.3.2 2.5.6 3.6.1.3 0 .7-.2 1z" fill="#333"/></svg>
      </span>
    </div>
  </header>

  <h1 class="hero-title">PRIVATE &amp; BUSINESS</h1>
  <div class="hero-sub">PERSONALISED TRANSPORT SERVICES</div>

  <section class="quote-panel">
    <h2 class="quote-title">GET INSTANT <b>QUOTE</b></h2>
    <div class="field field-origin">Origin</div>
    <div class="field field-dest">Destination</div>
    <div class="field field-vehicles">
      <div>Show other vehicles</div>
      <div class="add"><span>+</span><span>Add</span></div>
    </div>
    <div class="cta">GET STARTED NOW!</div>
  </section>

  <div class="hero-photo" role="img" aria-label="Photo of a dark luxury sedan driving at speed on a highway"></div>

  <section class="service" style="left:74px">
    <div class="service-icon">
      <svg width="32" height="22" viewBox="0 0 32 22"><path d="M6 9l3-6c.4-.8 1.2-1.3 2-1.3h10c.8 0 1.6.5 2 1.3l3 6h1.5c1 0 1.5.6 1.5 1.5v6c0 .8-.6 1.5-1.5 1.5H27v2a1.5 1.5 0 0 1-3 0v-2H8v2a1.5 1.5 0 0 1-3 0v-2H3.5C2.6 18 2 17.3 2 16.5v-6C2 9.6 2.6 9 3.5 9z" fill="#fff"/><path d="M9 9l2.3-4.6h9.4L23 9z" fill="#2f2f2f"/><circle cx="7" cy="13" r="2" fill="#2f2f2f"/><circle cx="25" cy="13" r="2" fill="#2f2f2f"/></svg>
    </div>
    <h3>CORPORATE <b>CARS</b></h3>
    <p>Lorem ipsum dolor sit amet, co nsectetuer adipiscing elit, sed diam nonummy nibh euismod Lorem ipsum dolor sit</p>
  </section>

  <section class="service" style="left:313px">
    <div class="service-icon">
      <svg width="34" height="28" viewBox="0 0 34 28"><circle cx="5" cy="3" r="2.6" fill="#fff"/><path d="M2 7h6v9H7v11H3V16H2z" fill="#fff"/><path d="M13 16l2.5-5c.3-.6.9-1 1.6-1h8.8c.7 0 1.3.4 1.6 1l2.5 5h1c.8 0 1.3.5 1.3 1.3v5c0 .7-.5 1.2-1.3 1.2H11.3c-.8 0-1.3-.5-1.3-1.2v-5c0-.8.5-1.3 1.3-1.3z" fill="#fff"/><path d="M15.5 16l1.8-3.7h8.4l1.8 3.7z" fill="#2f2f2f"/><circle cx="14" cy="24.5" r="2" fill="#fff"/><circle cx="28" cy="24.5" r="2" fill="#fff"/></svg>
    </div>
    <h3>LIMO <b>SERVICE</b></h3>
    <p>Lorem ipsum dolor sit amet, co nsectetuer adipiscing elit, sed diam nonummy nibh euismod Lorem ipsum dolor sit</p>
  </section>

  <section class="service" style="left:550px">
    <div class="service-icon">
      <svg width="32" height="24" viewBox="0 0 32 24"><path d="M4 10l3.2-7C7.6 2.2 8.4 1.6 9.3 1.6h13.4c.9 0 1.7.6 2.1 1.4L28 10h.5c1 0 1.5.6 1.5 1.5V19c0 .8-.6 1.5-1.5 1.5H28v1.5a1.5 1.5 0 0 1-3 0v-1.5H7v1.5a1.5 1.5 0 0 1-3 0v-1.5h-.5C2.6 20.5 2 19.8 2 19v-7.5C2 10.6 2.6 10 3.5 10z" fill="#fff"/><path d="M7 10l2.6-5.6h12.8L25 10z" fill="#2f2f2f"/><rect x="5" y="13" width="5" height="2.5" fill="#2f2f2f"/><rect x="22" y="13" width="5" height="2.5" fill="#2f2f2f"/></svg>
    </div>
    <h3>DISABILITY <b>TRANSIT</b></h3>
    <p>Lorem ipsum dolor sit amet, co nsectetuer adipiscing elit, sed diam nonummy nibh euismod Lorem ipsum dolor sit</p>
  </section>

  <section class="service" style="left:787px">
    <div class="service-icon">
      <svg width="30" height="28" viewBox="0 0 30 28"><rect x="9" y="1" width="12" height="3" fill="none" stroke="#fff" stroke-width="1.4"/><rect x="3" y="6" width="24" height="16" rx="3" fill="none" stroke="#fff" stroke-width="1.6"/><rect x="6" y="9" width="18" height="6" fill="none" stroke="#fff" stroke-width="1.4"/><line x1="15" y1="9" x2="15" y2="15" stroke="#fff" stroke-width="1.4"/><circle cx="8" cy="18.5" r="1.5" fill="#fff"/><circle cx="22" cy="18.5" r="1.5" fill="#fff"/><rect x="5" y="22" width="4" height="4" fill="#fff"/><rect x="21" y="22" width="4" height="4" fill="#fff"/></svg>
    </div>
    <h3>FAMILY <b>TRANSIT SERVICE.</b></h3>
    <p>Lorem ipsum dolor sit amet, co nsectetuer adipiscing elit, sed diam nonummy nibh euismod Lorem ipsum dolor sit</p>
  </section>

  <section class="about">
    <h2>ABOUT US</h2>
    <p>Lorem ipsum dolor sit amet, consectetuer adipiscing elit, sed diam nonummy nibh euismod Lorem ipsum dolor sit Lorem ipsum dolor sit amet, consectetuer adipiscing elit, sed diam nonummy nibh euismod Lorem ipsum dolor sit Lorem ipsum dolor sit amet, consectetuer adipiscing elit, sed diam nonummy nibh euismod Lorem ipsum dolor sit Lorem ipsum dolor sit amet, consectetuer adipiscing elit, sed diam nonummy nibh euismod Lorem ipsum dolor sit Lorem ipsum dolor sit amet, consectetuer adipiscing elit, sed diam nonummy nibh</p>
    <div class="about-frame">
      <div class="about-photo" role="img" aria-label="Photo of a black executive sedan in front of city skyscrapers"></div>
    </div>
  </section>

  <footer class="site-footer">Copyright © 2017 RIDEWAY. All right reserved.</footer>

</div>
</body>
</html>
```